Corporate Business Card

Very professional, Modern, Not to busy, include phone address email, website
(253) 555-0174, 61807 19th Street N, Kent, WA 98517, marcus@kestrelbayholding.com, brelvanindustries.com

Target Market(s)

Manufacturing

Industry/Entity Type

Aero, machining, manufacturing, Off road racing

Contact Information for Business Card

Phone, address email, website

```html
<!DOCTYPE html>
<html lang="en">
<head>
<meta charset="utf-8">
<title>Brelvan Industries — Business Card</title>
<link rel="stylesheet" href="https://fonts.googleapis.com/css2?family=Arimo:wght@400;700&display=swap">
<style>
  :root {
    --navy: #2c4478;
    --red: #d8303a;
    --paper: #fbfbfb;
    --ink: #1c1c1c;
    --white: #ffffff;
    --backdrop: #e7e7e9;
  }
  * { box-sizing: border-box; margin: 0; padding: 0; }
  html, body { width: 1200px; height: 900px; overflow: hidden; }
  body {
    background: var(--backdrop);
    font-family: "Arimo", Arial, sans-serif;
    position: relative;
  }
  .card {
    position: absolute;
    left: 320px;
    width: 560px;
    height: 320px;
    overflow: hidden;
    box-shadow: 0 6px 18px rgba(0,0,0,0.18);
  }
  /* front */
  .card-front { top: 95px; background: var(--paper); color: var(--ink); }
  .front-brand {
    position: absolute; left: 40px; top: 42px;
    font-weight: 700; font-size: 25px; letter-spacing: 0.5px;
    color: var(--navy);
  }
  .brand-rule {
    position: absolute; left: 40px; top: 84px; width: 470px; height: 1.5px;
    background: var(--navy);
  }
  .person {
    position: absolute; right: 40px; top: 40px; text-align: right;
  }
  .person-name { font-size: 22px; font-weight: 400; letter-spacing: 0.5px; }
  .person-title { font-size: 10.5px; letter-spacing: 0.6px; margin-top: 3px; }
  .contact-rule {
    position: absolute; left: 40px; top: 160px; width: 300px; height: 1.5px;
    background: var(--navy);
  }
  .contact-list {
    position: absolute; left: 40px; top: 176px; list-style: none;
    font-size: 11.5px; line-height: 21px;
  }
  .contact-list li { display: flex; align-items: center; gap: 12px; }
  .contact-list svg { width: 12px; height: 12px; flex: none; }
  .stripes { position: absolute; left: 0; bottom: 0; width: 560px; height: 50px; }
  /* back */
  .card-back { top: 485px; background: var(--navy); color: var(--white); }
  .back-brand {
    position: absolute; left: 0; right: 0; top: 118px; text-align: center;
    font-weight: 700; font-size: 44px; letter-spacing: 1px; color: var(--white);
  }
  .back-brand-rule {
    position: absolute; left: 140px; top: 182px; width: 280px; height: 1.5px;
    background: var(--white);
  }
  .back-footer {
    position: absolute; left: 0; right: 0; bottom: 34px;
    display: flex; align-items: center; gap: 14px;
  }
  .back-footer .line { flex: 1; height: 1.5px; background: var(--white); }
  .back-web { font-size: 15px; letter-spacing: 2.5px; }
</style>
</head>
<body>
  <section class="card card-front">
    <div class="front-brand">BRELVAN INDUSTRIES</div>
    <div class="brand-rule"></div>
    <div class="person">
      <div class="person-name">ELLIS MARLOW</div>
      <div class="person-title">BUSINESS MANAGER</div>
    </div>
    <div class="contact-rule"></div>
    <ul class="contact-list">
      <li><svg viewBox="0 0 12 12"><path d="M2.5 1 L4.5 1 L5.2 3.6 L4 4.6 Q5 7 7.4 8 L8.4 6.8 L11 7.5 L11 9.5 Q10.5 11 9 11 Q1 10 1 3 Q1 1.5 2.5 1Z" fill="var(--ink)"/></svg>(253) 555-0174</li>
      <li><svg viewBox="0 0 12 12"><path d="M6 11.5 L2.6 6.5 A4 4 0 1 1 9.4 6.5Z" fill="var(--ink)"/><circle cx="6" cy="4.3" r="1.5" fill="var(--paper)"/></svg>61807 19th Street N, Kent, WA 98517</li>
      <li><svg viewBox="0 0 12 12"><rect x="0.7" y="2.2" width="10.6" height="7.6" fill="none" stroke="var(--ink)" stroke-width="1"/><path d="M0.7 2.2 L6 6.8 L11.3 2.2" fill="none" stroke="var(--ink)" stroke-width="1"/></svg>marcus@kestrelbayholding.com</li>
      <li><svg viewBox="0 0 12 12"><g fill="none" stroke="var(--ink)" stroke-width="0.9"><circle cx="6" cy="6" r="5"/><ellipse cx="6" cy="6" rx="2.2" ry="5"/><path d="M1 6 H11 M2 3.3 H10 M2 8.7 H10"/></g></svg>www.brelvanindustries.com</li>
    </ul>
    <svg class="stripes" viewBox="0 0 560 50" preserveAspectRatio="none" aria-hidden="true">
      <polygon points="0,30 330,30 318,38 0,38" fill="var(--red)"/>
      <polygon points="330,30 560,0 560,8 318,38" fill="var(--navy)"/>
    </svg>
  </section>

  <section class="card card-back">
    <div class="back-brand">BRELVAN INDUSTRIES</div>
    <div class="back-brand-rule"></div>
    <div class="back-footer">
      <span class="line"></span>
      <span class="back-web">www.brelvanindustries.com</span>
      <span class="line"></span>
    </div>
  </section>
</body>
</html>
```